Storage Auctions Book Cover

I need a new cover for my book which is located here:
http://www.quillmart-example.com/dp/R417TZ2WQX/
The book is about making money by buying storage units at auction, made popular by the reality shows "Locker Clash" and "Gavel Trackers." It's for entrepreneurs and those looking for a weekend business.
The current cover was homemade in Gimp, and it's holding back sales. I think it needs a better cover in order to look more professional and catch more attention.
Updates
So far, I really like the designs from Pimbleworth and vostacraft. Consider those two what I'm looking for, they are both good.
Industry/Entity Type
Storage
Look and feel
Each slider illustrates characteristics of the customer's brand and the style your logo design should communicate.

```html
<!DOCTYPE html>
<html lang="en">
<head>
<meta charset="utf-8">
<title>Making Money in Storage Auctions — Book Cover</title>
<link rel="stylesheet" href="https://fonts.googleapis.com/css2?family=Anton&family=Raleway:wght@400&display=swap">
<style>
  :root {
    --canvas-bg: #ffffff;
    --band-black: #0b0b0b;
    --author-white: #f2f2f2;
    --wall-red-light: #e0435a;
    --wall-red: #c8102e;
    --wall-red-deep: #9e0c22;
    --door-white: #e9e9ea;
    --door-grey: #bdbdc0;
    --opening-black: #050505;
    --coin-gold: #3a2a06;
    --title-white: #ffffff;
    --subtitle-black: #000000;
  }
  * { margin: 0; padding: 0; box-sizing: border-box; }
  html, body {
    width: 1200px;
    height: 1000px;
    overflow: hidden;
    background: var(--canvas-bg);
  }
  .book-cover {
    position: absolute;
    left: 320px;
    top: 79px;
    width: 560px;
    height: 842px;
    overflow: hidden;
    background: var(--opening-black);
  }
  .author-band {
    position: absolute;
    left: 0; top: 0;
    width: 100%;
    height: 64px;
    background: var(--band-black);
    display: flex;
    align-items: center;
    justify-content: center;
    z-index: 2;
  }
  .author-name {
    font-family: "Raleway", sans-serif;
    font-weight: 400;
    font-size: 22px;
    letter-spacing: 0.42em;
    color: var(--author-white);
    text-transform: uppercase;
    padding-left: 0.42em;
  }
  .cover-photo {
    position: absolute;
    left: 0; top: 64px;
    width: 100%;
    height: 778px;
    background:
      linear-gradient(172deg,
        var(--wall-red-light) 0%,
        var(--wall-red) 30%,
        var(--wall-red-deep) 44%,
        var(--door-white) 46%,
        var(--door-grey) 64%,
        var(--opening-black) 67%,
        var(--coin-gold) 85%,
        var(--opening-black) 100%);
  }
  .cover-title {
    position: absolute;
    left: 276px;
    top: 268px;
    transform: translate(-50%, -50%) rotate(-15deg) skewX(-6deg);
    font-family: "Anton", sans-serif;
    font-size: 72px;
    line-height: 1.05;
    color: var(--title-white);
    text-align: center;
    text-transform: uppercase;
    white-space: nowrap;
    z-index: 2;
  }
  .cover-subtitle {
    position: absolute;
    left: 280px;
    top: 478px;
    transform: translate(-50%, -50%) rotate(-8deg);
    font-family: "Anton", sans-serif;
    font-size: 29px;
    line-height: 1.02;
    color: var(--subtitle-black);
    text-align: center;
    text-transform: uppercase;
    white-space: nowrap;
    z-index: 2;
  }
</style>
</head>
<body>
  <main class="book-cover">
    <header class="author-band">
      <p class="author-name">Dalton Merriweather</p>
    </header>
    <div class="cover-photo" role="img" aria-label="Red corrugated storage building with a half-open white roll-up door, gold dollar signs floating in the dark opening below"></div>
    <h1 class="cover-title">Making Money in<br>Storage Auctions</h1>
    <p class="cover-subtitle">How to profit from<br>the Locker Clash and<br>become a storage<br>auction warrior</p>
  </main>
</body>
</html>
```